House Builder and Property Development Card Design and Logo

I need a business card design for a building and property development company.
Colour scheme of Dark Grey and Green, I would like it bold, sharp and professional.
No logo yet done, I'm open to options but please stay away from the usual- house, roof, hammers etc.
Thanks Lou
Updates

Please be aware that on the business card information section the VKRT # 5382917 is a licence number and my phone number 0461739258. The numbers are close together and could be mistaken as one whole number 

Thank you

                                   

Industry/Entity Type

Building

Contact Information for Business Card

HARLOW BUILD & DEVELOPMENT.
Residential Building & Property Development
Louis Harlow - Director
VKRT # 5382917
0461739258
lou@harlowbuild.com.au

Requirements
Must have
• Bold Business name
Dark grey and green colours
Should not have
• roof outline or hammer logo

```html
<!DOCTYPE html>
<html lang="en">
<head>
<meta charset="utf-8">
<title>Harlow Build &amp; Development – Business Card</title>
<link rel="stylesheet" href="https://fonts.googleapis.com/css2?family=PT+Sans+Narrow:wght@400;700&display=swap">
<style>
  :root {
    --backdrop: #e4e5e6;
    --card-white: #ffffff;
    --steel-dark: #6f757a;
    --steel-mid: #8d9296;
    --steel-light: #b3b7ba;
    --brand-green: #13553d;
    --text-white: #ffffff;
    --card-w: 860px;
    --card-h: 529px;
  }
  * { margin: 0; padding: 0; box-sizing: border-box; }
  html, body {
    width: 1200px;
    height: 1184px;
    overflow: hidden;
    background: var(--backdrop);
    font-family: "PT Sans Narrow", "Arial Narrow", sans-serif;
  }
  .sheet {
    width: 1200px;
    height: 1184px;
    display: flex;
    flex-direction: column;
    align-items: center;
    justify-content: center;
    gap: 42px;
  }
  .card {
    position: relative;
    width: var(--card-w);
    height: var(--card-h);
    background: var(--card-white);
    overflow: hidden;
    box-shadow: 0 2px 10px rgba(0,0,0,0.12);
  }
  .steel-band {
    position: absolute;
    left: 0;
    width: 100%;
    background: linear-gradient(90deg,
      var(--steel-dark) 0%, var(--steel-mid) 22%, var(--steel-light) 42%,
      var(--steel-mid) 60%, var(--steel-dark) 80%, var(--steel-mid) 100%);
  }
  /* Contact side */
  .card--contact .steel-band { top: 148px; height: 208px; }
  .contact-name {
    position: absolute;
    left: 92px;
    top: 180px;
    color: var(--text-white);
    font-size: 24px;
    font-weight: 700;
  }
  .contact-name .role { font-style: italic; }
  .contact-details {
    position: absolute;
    left: 92px;
    top: 252px;
    color: var(--text-white);
    font-size: 18px;
    line-height: 26px;
    list-style: none;
  }
  .divider {
    position: absolute;
    left: 433px;
    top: 204px;
    width: 1px;
    height: 110px;
    background: rgba(255,255,255,0.85);
  }
  .brand-square {
    position: absolute;
    left: 566px;
    top: 150px;
    width: 204px;
    height: 204px;
    background: var(--brand-green);
  }
  /* Brand side */
  .card--brand .steel-band--top { top: 0; height: 148px; }
  .card--brand .steel-band--bottom { top: 356px; height: 173px; }
  .brand-lockup {
    position: absolute;
    left: 0;
    top: 148px;
    width: 100%;
    height: 208px;
    display: flex;
    align-items: center;
    justify-content: center;
    gap: 30px;
  }
  .brand-lockup .mark {
    width: 96px;
    height: 96px;
    background: var(--brand-green);
    flex: none;
  }
  .brand-name {
    color: var(--brand-green);
    font-weight: 700;
    text-transform: uppercase;
    line-height: 1;
  }
  .brand-name .line-main { display: block; font-size: 74px; letter-spacing: 2px; }
  .brand-name .line-sub { display: block; font-size: 33px; letter-spacing: 1px; margin-top: 6px; }
</style>
</head>
<body>
<main class="sheet">
  <section class="card card--contact" aria-label="Card front with contact details">
    <div class="steel-band"></div>
    <h1 class="contact-name">Louis Harlow - <span class="role">Director</span></h1>
    <ul class="contact-details">
      <li>VKRT # 5382917</li>
      <li>Phone: 0461 739 258</li>
      <li>Email: lou@harlowbuild.com.au</li>
    </ul>
    <div class="divider"></div>
    <div class="brand-square"></div>
  </section>

  <section class="card card--brand" aria-label="Card back with company name">
    <div class="steel-band steel-band--top"></div>
    <div class="brand-lockup">
      <div class="mark"></div>
      <h2 class="brand-name">
        <span class="line-main">Harlow</span>
        <span class="line-sub">Build &amp; Development</span>
      </h2>
    </div>
    <div class="steel-band steel-band--bottom"></div>
  </section>
</main>
</body>
</html>
```